Tallyden Web Design

Create Website Design for Tallyden. Tallyden is online application for collaboration team work system (task list management). More concept design for this project please find attach file ("tallyden website concept.pdf") . But my concept is just describe minimal features not bind design

For tallyden logo, i had already attach files. But i had not decided what color i chose, so it's okay if you suggest logo color for your suitable website design.
Updates

Dear All Designer,

I like brisk carousel (http://quillforge-labs.example/brisk-carousel/),
may be your concept design can adjust with this concept.
but don't worry about script for brisk carousel, my team will be handle
You just make website design to suitable with brisk carousel

but if you had own website design concept are welcome

thanks

Target Market(s)

Business Company

Industry/Entity Type

Management

```html
<!DOCTYPE html>
<html lang="fr">
<head>
<meta charset="utf-8">
<title>Tallyden — Online Collaboration Team Work</title>
<link rel="stylesheet" href="https://fonts.googleapis.com/css2?family=Open+Sans:ital,wght@0,300;0,400;0,600;0,700;1,400&display=swap">
<style>
:root{
  --ink:#2b2b2b;
  --muted:#7a7a7a;
  --teal:#3fa88d;
  --orange:#f28a1c;
  --red-orange:#e8502a;
  --black:#050505;
  --sky-top:#cfe6f7;
  --sky-bottom:#eaf5fc;
  --line:#e4e4e4;
  --panel:#f7f7f7;
}
*{box-sizing:border-box;margin:0;padding:0}
html,body{width:1137px;height:1200px;overflow:hidden;background:#fff}
body{position:relative;font-family:"Open Sans",sans-serif;color:var(--ink)}
.abs{position:absolute}

/* header */
.topbar{left:0;top:0;width:1137px;height:74px;background:var(--black)}
.brand{left:162px;top:16px;display:flex;align-items:center;gap:10px}
.brand-dot{width:22px;height:22px;border-radius:50%;background:var(--teal)}
.brand-name{font-size:34px;font-weight:600;color:var(--orange);letter-spacing:-.5px;line-height:1}
.existing{right:274px;top:29px;font-size:11px;font-style:italic;color:#d9d9d9;white-space:nowrap}
.signin{left:879px;top:21px;width:95px;height:35px;border-radius:18px;background:var(--orange);color:#fff;font-size:19px;display:flex;align-items:center;justify-content:center;letter-spacing:.3px}

/* navigation */
.nav{left:0;top:74px;width:1137px;height:47px;background:linear-gradient(#fdfdfd,#eef0f1);border-bottom:1px solid #dfe3e6}
.nav-item{top:16px;font-size:13px;color:#444;letter-spacing:.2px}
.nav-sep{top:14px;width:1px;height:20px;background:#dcdcdc}
.nav-active{left:164px;top:9px;width:83px;height:30px;border-radius:15px;background:var(--teal);color:#fff;font-size:13px;display:flex;align-items:center;justify-content:center}
.phone{left:818px;top:12px;display:flex;align-items:center;gap:12px;color:var(--teal);font-size:16px}

/* hero */
.hero{left:0;top:121px;width:1137px;height:365px;background:linear-gradient(180deg,var(--sky-top),var(--sky-bottom))}
.hero-figure{left:162px;top:32px;width:384px;height:292px;background:linear-gradient(90deg,#d7edf8 0 52%,#e6e6e4 52%);border:3px solid #e9f3fa;box-shadow:0 4px 10px rgba(0,80,130,.12)}
.hero-title{left:583px;top:52px;width:460px;font-size:28px;font-weight:300;color:var(--teal);line-height:33px;letter-spacing:-.2px}
.hero-title b{color:#333;font-weight:600}
.hero-text{left:583px;top:129px;width:400px;font-size:15.5px;font-weight:300;line-height:29px;color:#333}
.btn-more{left:583px;top:263px;width:83px;height:30px;border-radius:15px;background:var(--teal);color:#fff;font-size:11px;display:flex;align-items:center;justify-content:center;box-shadow:0 0 0 2px rgba(255,255,255,.5)}
.dots{left:918px;top:338px;display:flex;gap:6px}
.dots span{width:10px;height:10px;border-radius:50%;background:#cfe2ef}
.dots span.on{background:#a6cde6}

/* features */
.card{top:567px;width:252px}
.card-media{height:113px}
.card-badge{position:absolute;left:100px;top:-25px;width:52px;height:52px;border-radius:50%;background:var(--red-orange);border:3px solid #fff;box-shadow:0 1px 3px rgba(0,0,0,.25);display:flex;align-items:center;justify-content:center}
.card h3{margin-top:17px;text-align:center;font-weight:400;font-size:16px;color:var(--red-orange);letter-spacing:.2px}
.card p{margin-top:6px;text-align:center;font-size:10.5px;line-height:14.6px;color:#555;padding:0 10px}
.card-rule{position:absolute;left:0;top:213px;width:252px;height:1px;background:var(--line)}

/* section headings */
.sec-head{top:843px;display:flex;align-items:center;gap:12px;font-size:16px;color:#333}
.sec-head i{display:block;height:5px;border-top:1px solid var(--line);border-bottom:1px solid var(--line);flex:1}

/* accordion */
.accordion{left:170px;top:886px;width:370px;border:1px solid #ececec}
.acc-row{display:flex;align-items:flex-start;gap:12px;padding:12px 18px 0 18px;border-bottom:1px solid #ececec;background:var(--panel)}
.acc-row.open{background:#fff;padding-bottom:10px}
.acc-row:last-child{border-bottom:none}
.acc-row svg{flex:none}
.acc-title{font-size:14px;line-height:20px;color:#2b2b2b}
.acc-row.closed{height:43px}
.acc-body{margin-top:4px;font-size:11px;line-height:16.2px;color:var(--muted)}

/* who we are */
.who-img{left:598px;top:886px;width:104px;height:105px;background:radial-gradient(circle at 55% 55%,#e0a24a 0 12%,#2d6f86 35%,#0e2838 80%)}
.who-text{left:723px;top:882px;width:243px;font-size:11px;line-height:16.2px;color:var(--muted)}
.quote{left:598px;top:1004px;width:364px;height:44px;background:var(--panel);border-left:4px solid var(--teal);padding:6px 14px;font-size:11px;line-height:16.2px;color:var(--muted)}
.who-more{left:598px;top:1060px;width:370px;font-size:11px;line-height:16.2px;color:var(--muted)}

/* footer */
.foot-rule{left:170px;top:1145px;width:793px;height:1px;background:var(--line)}
.foot-links{left:170px;top:1164px;font-size:10px;color:#333}
.foot-links span{margin:0 5px;color:#999}
.foot-copy{right:175px;top:1164px;font-size:10px;color:#333}
</style>
</head>
<body>

<header>
  <div class="abs topbar"></div>
  <div class="abs brand"><span class="brand-name">tallyden</span><span class="brand-dot"></span></div>
  <div class="abs existing">Already an existing Tallyden Customer?</div>
  <a class="abs signin">SIGN IN</a>
</header>

<nav class="abs nav">
  <a class="abs nav-active">FEATURES</a>
  <span class="abs nav-sep" style="left:268px"></span>
  <a class="abs nav-item" style="left:297px">PRICING</a>
  <span class="abs nav-sep" style="left:377px"></span>
  <a class="abs nav-item" style="left:411px">SECURITY</a>
  <span class="abs nav-sep" style="left:501px"></span>
  <a class="abs nav-item" style="left:538px">FAQ</a>
  <span class="abs nav-sep" style="left:598px"></span>
  <a class="abs nav-item" style="left:636px">PROJECTS</a>
  <div class="abs phone">
    <svg width="14" height="18" viewBox="0 0 14 18"><rect x="1" y="1" width="12" height="16" rx="1.5" fill="var(--teal)"/><rect x="3" y="3" width="8" height="4" fill="#fff"/><g fill="#fff"><rect x="3" y="9" width="2" height="2"/><rect x="6" y="9" width="2" height="2"/><rect x="9" y="9" width="2" height="2"/><rect x="3" y="12" width="2" height="2"/><rect x="6" y="12" width="2" height="2"/><rect x="9" y="12" width="2" height="2"/></g></svg>
    <span>555 014 2290</span>
  </div>
</nav>

<section class="abs hero">
  <div class="abs hero-figure" role="img" aria-label="Diagram of automatic task creation and distribution between managers, shoppers, associates and mobile workforce software"></div>
  <h1 class="abs hero-title">Customize <b>Online</b> Collaboration<br><b>Team</b> Work</h1>
  <p class="abs hero-text">On sait depuis longtemps que travailler avec du texte lisible et contenant du sens est source de distractions, et empêche de se concentrer sur la mise en page elle-même.</p>
  <a class="abs btn-more">READ MORE</a>
  <div class="abs dots"><span class="on"></span><span></span><span></span><span></span></div>
</section>

<section>
  <article class="abs card" style="left:171px">
    <div class="card-media" role="img" aria-label="Screenshot of an application setup screen" style="background:linear-gradient(#d8d8d8,#eeeeee 20%,#f6f6f6)"></div>
    <div class="card-badge"><svg width="28" height="28" viewBox="0 0 28 28"><circle cx="14" cy="14" r="9" fill="none" stroke="#fff" stroke-width="5" stroke-dasharray="4 3"/><circle cx="14" cy="14" r="5" fill="#fff"/><circle cx="14" cy="14" r="3" fill="var(--red-orange)"/></svg></div>
    <h3>CUSTOMIZE APPLICATION</h3>
    <p>Le Lorem Ipsum est simplement du faux texte employé dans la composition et la mise en page avant impression.</p>
    <div class="card-rule"></div>
  </article>
  <article class="abs card" style="left:447px">
    <div class="card-media" role="img" aria-label="Illustration of devices linked around a cloud" style="background:radial-gradient(circle at 50% 50%,#2d6a8a,#0a1a26 60%,#050a10)"></div>
    <div class="card-badge"><svg width="22" height="24" viewBox="0 0 22 24"><rect x="3" y="2" width="16" height="20" rx="2" fill="none" stroke="#fff" stroke-width="2.5"/><rect x="6" y="5" width="10" height="12" fill="#fff" opacity=".35"/></svg></div>
    <h3>SYNCHRONIZE ALL DEVICE</h3>
    <p>Le Lorem Ipsum est simplement du faux texte employé dans la composition et la mise en page avant impression.</p>
    <div class="card-rule"></div>
  </article>
  <article class="abs card" style="left:723px">
    <div class="card-media" role="img" aria-label="Infographic with numbered report steps" style="background:#a9a9a9"></div>
    <div class="card-badge"><svg width="26" height="24" viewBox="0 0 26 24"><rect x="8" y="3" width="15" height="16" fill="none" stroke="#fff" stroke-width="2"/><g stroke="#fff" stroke-width="2"><line x1="11" y1="8" x2="20" y2="8"/><line x1="11" y1="12" x2="20" y2="12"/></g><line x1="3" y1="21" x2="12" y2="12" stroke="#fff" stroke-width="3"/></svg></div>
    <h3>REPORT</h3>
    <p>Le Lorem Ipsum est simplement du faux texte employé dans la composition et la mise en page avant impression.</p>
    <div class="card-rule"></div>
  </article>
</section>

<section>
  <h2 class="abs sec-head" style="left:170px;width:370px;font-weight:400">WHAT WE DO <i></i></h2>
  <div class="abs accordion">
    <div class="acc-row closed">
      <svg width="20" height="20" viewBox="0 0 20 20"><circle cx="10" cy="10" r="10" fill="var(--teal)"/><circle cx="10" cy="10" r="6.5" fill="none" stroke="#fff" stroke-width="1.2"/><path d="M10 6.5v7M6.5 10h7" stroke="#fff" stroke-width="1.6"/></svg>
      <div class="acc-title">Contrairement à une opinion répandue.</div>
    </div>
    <div class="acc-row open">
      <svg width="20" height="20" viewBox="0 0 20 20"><circle cx="10" cy="10" r="10" fill="var(--teal)"/><circle cx="10" cy="10" r="6.5" fill="none" stroke="#fff" stroke-width="1.2"/><path d="M6.5 10h7" stroke="#fff" stroke-width="1.6"/></svg>
      <div>
        <div class="acc-title">Du texte.' est qu'il possède</div>
        <p class="acc-body">anonyme assembla ensemble des morceaux de texte pour réaliser un livre spécimen de polices de texte. Il n'a pas fait que survivre cinq siècles,</p>
      </div>
    </div>
    <div class="acc-row closed">
      <svg width="20" height="20" viewBox="0 0 20 20"><circle cx="10" cy="10" r="10" fill="var(--teal)"/><circle cx="10" cy="10" r="6.5" fill="none" stroke="#fff" stroke-width="1.2"/><path d="M10 6.5v7M6.5 10h7" stroke="#fff" stroke-width="1.6"/></svg>
      <div class="acc-title">Du français standard de nombreuses</div>
    </div>
    <div class="acc-row closed">
      <svg width="20" height="20" viewBox="0 0 20 20"><circle cx="10" cy="10" r="10" fill="var(--teal)"/><circle cx="10" cy="10" r="6.5" fill="none" stroke="#fff" stroke-width="1.2"/><path d="M10 6.5v7M6.5 10h7" stroke="#fff" stroke-width="1.6"/></svg>
      <div class="acc-title">Un professeur du Ashcombe-Vale College</div>
    </div>
  </div>
</section>

<section>
  <h2 class="abs sec-head" style="left:597px;width:377px;font-weight:400">WHO WE ARE <i></i></h2>
  <div class="abs who-img" role="img" aria-label="Photo of a tablet showing business charts"></div>
  <p class="abs who-text">L'extrait standard de Lorem Ipsum utilisé depuis le XVIè siècle est reproduit ci-dessous pour les curieux. Les sections 1.10.32 et 1.10.33 du "De Finibus Bonorum et Malorum" de Varrius sont aussi reproduites dans leur version originale, accompagnée de la traduction anglaise de J. Telmore</p>
  <blockquote class="abs quote">Le Lorem Ipsum est simplement du faux texte employé dans la composition et la mise en page avant impression.</blockquote>
  <p class="abs who-more">Plusieurs variations de Lorem Ipsum peuvent être trouvées ici ou là, mais la majeure partie d'entre elles a été altérée par l'addition d'humour ou de mots aléatoires.</p>
</section>

<footer>
  <div class="abs foot-rule"></div>
  <div class="abs foot-links">Features<span>|</span>Pricing<span>|</span>Security<span>|</span>FAQ<span>|</span>Projects</div>
  <div class="abs foot-copy">© Copyrights 2013 All rights Reserved</div>
</footer>

</body>
</html>
```